WAYmaker website redesign to provide information about experiential workshops, film work and other

We need a redesign of our website waymakerhub.org. We conduct experiential workshops of discovery and transformation for individuals and organizations. We need the website to reflect the full extent of WAYmaker programs, and be an information hub for WAYmaker workshops and communities as they develop.

The attached documents contain information about the organization - it's brandbook, copy for web pages, a website layout and a couple of images.

The site is for individuals and companies looking to promote and be change to make a difference. It should be warm, welcoming, and create excitement around the concepts and the ability to discover a new way of being in the world. We are about creating communities around the globe who will embody play, freedom, curiosity and expanded possibilities. We are creating a space for this to happen, both physically (workshops) and online.

We will be on either a SquareSpace, but mos tlikely a Weebly plaform.

Please look at the current site at www.waymakerhub.org

Target Market(s)

Initially, are target market will be baby boomers, but will expand to include millennials and students.

Coding

Coded - Design and coding required

Number of Pages Required

5+ page

Requirements
Must have
• The colors, logo and fonts from the brand book.
Nice to have
• Complimentary use of brand colors to create an attractive presentation and energy

```html
<!DOCTYPE html>
<html lang="en">
<head>
<meta charset="utf-8">
<title>WAYmaker</title>
<link href="https://fonts.googleapis.com/css2?family=Overpass:wght@400;600;700&family=Hind:wght@300;400;500;600&display=swap" rel="stylesheet">
<style>
:root{
  --pink:#f7c5bd;
  --mauve:#a86a72;
  --mauve-dark:#94585f;
  --cream:#f6e2d3;
  --slate:#5c5c5c;
  --ink:#222;
  --text:#444;
  --muted:#8a8a8a;
  --footer:#2c2c2c;
  --white:#fff;
}
*{box-sizing:border-box;margin:0;padding:0}
html,body{width:1200px;height:2975px;overflow:hidden;background:var(--white)}
body{position:relative;font-family:"Hind",sans-serif;color:var(--text)}
.abs{position:absolute}
.photo{position:absolute}
.head{font-family:"Overpass",sans-serif;font-weight:600;letter-spacing:.3px}

/* hero */
.hero-photo{left:0;top:0;width:600px;height:575px;background:linear-gradient(160deg,#4a4a46 0%,#2f302c 55%,#3c4a38 100%)}
.hero-panel{left:600px;top:0;width:600px;height:515px;background:var(--slate)}
.logo{font-family:"Overpass",sans-serif;font-weight:700;color:var(--white);font-size:30px;letter-spacing:3px;display:flex;align-items:center;gap:10px}
.logo .mark{width:14px;height:14px;background:currentColor}
.socials{left:902px;top:36px;display:flex;gap:5px}
.socials span{width:22px;height:22px;border:1.5px solid var(--white);border-radius:50%}
.burger{left:1012px;top:36px;width:26px}
.burger i{display:block;height:2.5px;background:var(--white);margin-bottom:5px}
.dots{display:grid;grid-template-columns:repeat(3,5px);gap:5px}
.dots i{width:5px;height:5px;background:var(--white);border-radius:1px}
.hero-title{font-size:58px;line-height:64px;color:var(--cream)}
.hero-title.left{left:163px;top:248px;width:400px;color:#f2cabf}
.hero-title.right{left:635px;top:155px;width:420px}
.link-more{font-family:"Overpass",sans-serif;font-size:11px;font-weight:700;letter-spacing:1px;color:var(--mauve);display:flex;align-items:center;gap:10px}
.circle-arrow{width:22px;height:22px}

/* sections */
.pink-block{left:0;top:575px;width:600px;height:545px;background:var(--pink)}
.section-title{font-size:34px;line-height:45px;color:var(--mauve)}
.label{font-family:"Overpass",sans-serif;font-weight:700;font-size:13px;letter-spacing:.5px;color:var(--ink);border-bottom:2px solid var(--ink);padding-bottom:1px}
.bullets{list-style:none;font-size:12px;color:var(--ink)}
.bullets li{display:flex;align-items:center;gap:12px;height:25px}
.bullets li::before{content:"";width:7px;height:7px;border:1.5px solid var(--ink)}
.vlabel{font-family:"Overpass",sans-serif;font-size:10px;letter-spacing:2.5px;color:var(--mauve);transform:rotate(90deg);transform-origin:left top;white-space:nowrap}
.vlabel.up{transform:rotate(-90deg)}
.body-copy{font-size:13px;line-height:24px;color:var(--text)}
.body-copy p+p{margin-top:14px}
.btn{display:flex;align-items:center;justify-content:center;gap:12px;background:var(--mauve);color:var(--white);font-family:"Overpass",sans-serif;font-weight:700;font-size:11px;letter-spacing:.8px;width:135px;height:46px}
.grid-lines{left:0;top:1120px;width:1200px;height:1012px;background:repeating-linear-gradient(90deg,transparent 0 119px,#f3f3f3 119px 120px)}

/* card */
.card-stack{left:240px;top:2260px;width:720px;height:270px;background:#f4f4f4;box-shadow:0 6px 14px rgba(0,0,0,.06)}
.card{left:218px;top:2201px;width:764px;height:298px;background:var(--white);box-shadow:0 4px 22px rgba(0,0,0,.13);text-align:center;padding-top:48px}
.card h3{font-family:"Overpass",sans-serif;font-weight:600;color:var(--mauve);font-size:21px}
.card p{font-size:12px;line-height:20px;color:var(--muted);width:640px;margin:8px auto 0}
.card hr{border:0;border-top:1px solid #ddd;width:370px;margin:22px auto 18px}

/* footer */
.footer{left:0;top:2588px;width:1200px;height:387px;background:var(--footer);color:#bbb}
.cta-title{font-family:"Overpass",sans-serif;font-weight:700;font-size:17px;color:var(--white)}
.cta-sub{font-size:12px;color:#777}
.fbtn{font-family:"Overpass",sans-serif;font-weight:700;font-size:10px;letter-spacing:.5px;width:93px;height:37px;display:flex;align-items:center;justify-content:center;color:var(--ink)}
.fbtn.pink{background:var(--pink)}
.fbtn.white{background:var(--white)}
.col-title{font-family:"Overpass",sans-serif;font-weight:600;font-size:14px;color:var(--white);padding-bottom:8px;position:relative}
.col-title::after{content:"";position:absolute;left:0;bottom:0;width:150px;height:1px;background:linear-gradient(90deg,var(--pink),transparent)}
.links{list-style:none;font-size:11px;line-height:23px;color:#999}
.contact{font-size:11px;color:#999;line-height:18px}
.contact .row{display:flex;gap:18px;margin-bottom:16px}
.contact svg{flex:none;margin-top:2px}
.fsocials{display:flex;gap:5px}
.fsocials span{width:22px;height:22px;border:1.5px solid #999;border-radius:50%}
</style>
</head>
<body>

<!-- hero -->
<div class="photo hero-photo" role="img" aria-label="Group of people gathered outdoors in front of a wooden barn wall hung with framed artwork"></div>
<div class="abs hero-panel"></div>
<div class="abs logo" style="left:160px;top:33px"><span class="mark"></span>WAYMAKER</div>
<div class="abs socials"><span></span><span></span><span></span></div>
<div class="abs burger"><i></i><i></i><i></i></div>
<div class="abs dots" style="left:163px;top:192px"><i></i><i></i><i></i><i></i><i></i><i></i></div>
<h1 class="abs head hero-title left">What World Do We Want to Live In?</h1>
<h2 class="abs head hero-title right">What Kind of Life Do You Want to Create?</h2>
<div class="abs dots" style="left:1006px;top:464px"><i></i><i></i><i></i><i></i><i></i><i></i></div>
<div class="abs link-more" style="left:623px;top:541px">LEARN MORE
  <svg class="circle-arrow" viewBox="0 0 22 22"><circle cx="11" cy="11" r="10" fill="none" stroke="#a86a72" stroke-width="1.5"/><path d="M6 11h9M11 7l4 4-4 4" fill="none" stroke="#a86a72" stroke-width="1.5"/></svg>
</div>
<svg class="abs" style="left:1004px;top:537px" width="34" height="30" viewBox="0 0 34 30"><path d="M17 1L31 15 17 29 3 15Z" fill="none" stroke="#d9a9a6" stroke-width="1.3"/><path d="M15 9l-6 6 6 6M19 9l6 6-6 6" fill="none" stroke="#d9a9a6" stroke-width="1.3"/></svg>

<!-- discover -->
<div class="abs pink-block"></div>
<h2 class="abs head section-title" style="left:163px;top:638px;width:300px">Discover an Opportunity to Live a More Dynamic and Meaningful Life</h2>
<div class="abs label" style="left:163px;top:888px">WAYMAKER</div>
<ul class="abs bullets" style="left:163px;top:936px">
  <li>Moves Energy</li>
  <li>Creates Opportunities for Connecting</li>
  <li>Supports Conscious Evolution</li>
  <li>Deepens Experience of Life</li>
  <li>Provides Opportunities for Collaboration and Creation</li>
</ul>
<div class="photo" style="left:524px;top:674px;width:440px;height:327px;background:linear-gradient(150deg,#6e6e6e,#3a3a3a 60%,#8a8a8a)" role="img" aria-label="Black and white photo of workshop participants seated in a circle on a rug"></div>
<div class="abs vlabel" style="left:1038px;top:805px">WAYMAKER</div>

<!-- vision -->
<div class="abs grid-lines"></div>
<h2 class="abs head section-title" style="left:160px;top:1240px">Vision</h2>
<div class="abs body-copy" style="left:160px;top:1308px;width:386px">
  <p>We envision a world in which all people and communities can challenge and break free from stories that no longer serve us. We believe that solutions to contemporary challenges will emerge from a place of curiosity, love and connection.</p>
  <p>Through inspiration, conscious reflection, and collaboration, we take responsibility for the world we are manifesting, and we can discover and create new possibilities for the lives and the society we desire to build.</p>
</div>
<div class="abs btn" style="left:160px;top:1543px">LEARN MORE
  <svg class="circle-arrow" viewBox="0 0 22 22"><circle cx="11" cy="11" r="10" fill="none" stroke="#fff" stroke-width="1.5"/><path d="M6 11h9M11 7l4 4-4 4" fill="none" stroke="#fff" stroke-width="1.5"/></svg>
</div>
<div class="abs vlabel up" style="left:60px;top:1412px">WAYMAKER</div>
<div class="photo" style="left:600px;top:1120px;width:600px;height:506px;background:linear-gradient(165deg,#8c8c8c,#505050 45%,#2e2e2e)" role="img" aria-label="Black and white photo of a group seated in a bright wood-panelled room with tall windows"></div>

<!-- what we do -->
<div class="photo" style="left:0;top:1626px;width:600px;height:506px;background:linear-gradient(160deg,#6a6a6a,#3c3c3c 55%,#7a7a7a)" role="img" aria-label="Black and white photo of two facilitators seated in armchairs in conversation"></div>
<h2 class="abs head section-title" style="left:674px;top:1692px">What We Do</h2>
<div class="abs label" style="left:674px;top:1752px">WAYMAKER LIFE</div>
<div class="abs body-copy" style="left:674px;top:1788px;width:250px;font-size:12.5px;line-height:23px">WAYmaker Life is a workshop designed to re-engage you with life. Through interactive exercises and personal exploration, you are taken on a journey that ultimately leaves you experiencing life as a Creator.</div>
<ul class="abs bullets" style="left:674px;top:1921px">
  <li>Curiosity</li>
  <li>Awareness</li>
  <li>Own Your Creation</li>
  <li>Reimagine</li>
  <li>Manifest</li>
</ul>
<div class="abs btn" style="left:674px;top:2064px">LEARN MORE
  <svg class="circle-arrow" viewBox="0 0 22 22"><circle cx="11" cy="11" r="10" fill="none" stroke="#fff" stroke-width="1.5"/><path d="M6 11h9M11 7l4 4-4 4" fill="none" stroke="#fff" stroke-width="1.5"/></svg>
</div>
<div class="abs vlabel" style="left:1038px;top:1836px">WAYMAKER</div>

<!-- card -->
<div class="abs card-stack"></div>
<div class="abs card">
  <h3>Stirring the Still</h3>
  <p>The Stirring the Still workshop—an extension of the documentary of the same name—is an experiential process to transform participants into disturbers of the status quo within themselves, to enhance their relationships with others, and to change the environments in which they exist—and ultimately society—for the better.</p>
  <hr>
  <h3>In Your Community</h3>
  <p style="width:480px">Bring WAYmaker or the Stirring the Still workshop to your community. We would love to hear from you. Please fill out the brief form here</p>
</div>

<!-- footer -->
<div class="abs footer"></div>
<div class="abs cta-title" style="left:160px;top:2658px">Ready To Get Started ?</div>
<div class="abs cta-sub" style="left:160px;top:2688px">Get In Touch, or Create an Account</div>
<div class="abs fbtn pink" style="left:839px;top:2660px">GET STARTED</div>
<div class="abs fbtn white" style="left:946px;top:2660px">SIGN UP</div>

<div class="abs logo" style="left:160px;top:2774px;font-size:24px"><span class="mark" style="width:11px;height:11px"></span>WAYMAKER</div>
<div class="abs fsocials" style="left:160px;top:2820px"><span></span><span></span><span></span></div>
<div class="abs contact" style="left:160px;top:2862px;line-height:16px">© Copyright 2018 WAYmaker<br>All Rights Reserved.</div>

<div class="abs col-title" style="left:416px;top:2770px">Keep in Touch</div>
<div class="abs contact" style="left:416px;top:2820px;width:200px">
  <div class="row"><svg width="12" height="12" viewBox="0 0 12 12"><path d="M2 1l2 0 1 3-1.5 1a7 7 0 0 0 3.5 3.5L8 7l3 1v2a1 1 0 0 1-1 1A9 9 0 0 1 1 2a1 1 0 0 1 1-1z" fill="#999"/></svg><span>555.014.2270</span></div>
  <div class="row"><svg width="12" height="14" viewBox="0 0 12 14"><path d="M6 0a5 5 0 0 1 5 5c0 4-5 9-5 9S1 9 1 5a5 5 0 0 1 5-5z" fill="#999"/><circle cx="6" cy="5" r="2" fill="#2c2c2c"/></svg><span>Lorem Ipsum is simply dummy text of the printing</span></div>
  <div class="row"><svg width="13" height="10" viewBox="0 0 13 10"><rect x=".5" y=".5" width="12" height="9" fill="none" stroke="#999"/><path d="M.5.5l6 5 6-5" fill="none" stroke="#999"/></svg><span>hello@waymakerhub.org</span></div>
</div>

<div class="abs col-title" style="left:716px;top:2770px">Quick Links</div>
<ul class="abs links" style="left:716px;top:2820px">
  <li>About</li><li>Workshop</li><li>WAYmaker Projects</li><li>Films</li><li>Store &amp; Resources</li>
</ul>
<ul class="abs links" style="left:924px;top:2820px">
  <li>Community</li><li>Contact Us</li><li>Terms and Condition</li><li>Privacy Policy</li>
</ul>

</body>
</html>
```